Business Card Design needed for logo design project

Professional English School and translation company needs a business card design.

Target Market(s)

Wealthy business men. My company is called Summit Language Partners.

Requirements
Must have
• I would like it to be a dark color with my logo.

```html
<!DOCTYPE html>
<html lang="en">
<head>
<meta charset="utf-8">
<title>Summit Language Partners – Business Card</title>
<link rel="stylesheet" href="https://fonts.googleapis.com/css2?family=Poppins:wght@300;400;500;600&display=swap">
<style>
  :root {
    --stage: #2b2b2e;
    --card-white: #ffffff;
    --card-white-shade: #ececef;
    --slate: #5b5868;
    --slate-dark: #45434f;
    --slate-light: #6c6979;
    --orange: #f28c1c;
    --text-light: #f4f3f7;
    --text-muted: #d9d7e0;
  }
  * { box-sizing: border-box; margin: 0; padding: 0; }
  html, body {
    width: 1200px; height: 900px; overflow: hidden;
    background: var(--stage);
    font-family: "Poppins", sans-serif;
  }
  .stage {
    width: 1200px; height: 900px;
    display: flex; flex-direction: column; align-items: center; justify-content: center;
    gap: 50px;
  }
  .card {
    width: 560px; height: 320px;
    border-radius: 22px;
    overflow: hidden;
    position: relative;
    box-shadow: 0 12px 30px rgba(0,0,0,.45);
  }

  /* Front */
  .card-front { background: var(--slate); display: flex; flex-direction: column; }
  .front-top {
    height: 168px;
    background: linear-gradient(180deg, var(--card-white) 0%, var(--card-white-shade) 100%);
    display: flex; align-items: flex-end;
    padding: 0 0 30px 40px;
  }
  .brand { display: flex; align-items: center; gap: 14px; }
  .brand-dot { width: 44px; height: 44px; border-radius: 50%; background: var(--orange); flex: none; }
  .brand-name { font-weight: 600; font-size: 27px; line-height: 1; color: var(--slate-dark); letter-spacing: -.2px; white-space: nowrap; }
  .accent-stripe { height: 7px; background: var(--orange); }
  .front-bottom {
    flex: 1;
    background: linear-gradient(160deg, var(--slate-light) 0%, var(--slate) 55%, var(--slate-dark) 100%);
    display: flex; justify-content: space-between; gap: 16px;
    padding: 20px 30px 0 40px;
    color: var(--text-light);
  }
  .holder-line { display: flex; align-items: baseline; gap: 8px; margin-bottom: 12px; white-space: nowrap; }
  .holder-name { color: var(--orange); font-weight: 500; font-size: 19px; letter-spacing: .3px; text-transform: uppercase; }
  .holder-role { font-size: 11px; font-weight: 500; color: var(--text-light); }
  .contact-list { list-style: none; display: flex; flex-direction: column; gap: 6px; }
  .contact-item { display: flex; align-items: center; gap: 10px; font-size: 11px; font-weight: 300; color: var(--text-muted); white-space: nowrap; }
  .contact-icon { width: 13px; height: 13px; flex: none; }
  .office {
    align-self: flex-start;
    margin-top: 4px;
    border-left: 1px solid rgba(255,255,255,.55);
    padding-left: 12px;
    font-size: 10px; font-weight: 300; line-height: 1.55; font-style: normal;
    color: var(--text-muted);
    white-space: nowrap;
  }

  /* Back */
  .card-back {
    background:
      radial-gradient(ellipse at 40% 35%, rgba(255,255,255,.08) 0%, rgba(255,255,255,0) 60%),
      linear-gradient(160deg, var(--slate-light) 0%, var(--slate) 50%, var(--slate-dark) 100%);
    display: flex; align-items: center; justify-content: center;
  }
  .card-back .brand-dot { width: 58px; height: 58px; }
  .card-back .brand-name { color: var(--text-light); font-size: 30px; }
</style>
</head>
<body>
<main class="stage">
  <section class="card card-front" aria-label="Business card front">
    <div class="front-top">
      <div class="brand">
        <span class="brand-dot"></span>
        <span class="brand-name">Summit Language Partners</span>
      </div>
    </div>
    <div class="accent-stripe"></div>
    <div class="front-bottom">
      <div class="holder">
        <p class="holder-line">
          <span class="holder-name">Daniel Hartley</span>
          <span class="holder-role">| Consultant</span>
        </p>
        <ul class="contact-list">
          <li class="contact-item">
            <svg class="contact-icon" viewBox="0 0 16 16" aria-hidden="true"><rect x="4" y="1.5" width="8" height="13" rx="1.5" fill="none" stroke="#f28c1c" stroke-width="1.5"/><circle cx="8" cy="12" r="0.9" fill="#f28c1c"/></svg>
            +1 555 014 2287
          </li>
          <li class="contact-item">
            <svg class="contact-icon" viewBox="0 0 16 16" aria-hidden="true"><rect x="1.5" y="3.5" width="13" height="9" rx="1" fill="none" stroke="#f28c1c" stroke-width="1.5"/><path d="M2 4.5 8 9l6-4.5" fill="none" stroke="#f28c1c" stroke-width="1.5"/></svg>
            dan@summitlanguagepartners.com
          </li>
          <li class="contact-item">
            <svg class="contact-icon" viewBox="0 0 16 16" aria-hidden="true"><circle cx="8" cy="8" r="6.3" fill="none" stroke="#f28c1c" stroke-width="1.5"/><path d="M1.7 8h12.6M8 1.7c2.2 2.2 2.2 10.4 0 12.6M8 1.7c-2.2 2.2-2.2 10.4 0 12.6" fill="none" stroke="#f28c1c" stroke-width="1.1"/></svg>
            www.summitlanguagepartners.com
          </li>
        </ul>
      </div>
      <address class="office">
        Summit Language Partners<br>
        27 Harbour Lane, Suite 4,<br>
        Kingsport, Westmarch
      </address>
    </div>
  </section>

  <section class="card card-back" aria-label="Business card back">
    <div class="brand">
      <span class="brand-dot"></span>
      <span class="brand-name">Summit Language Partners</span>
    </div>
  </section>
</main>
</body>
</html>
```